Business card design needed

Business Card design required for new small plumbing business.
Would like a logo/text look that is simple and unique and does not have to be representative of a plumbing company (ie. having a cartoon plumber or toilet etc) as the companyname is self explanatory.
Would like the main colour to be green (lime green).

Industry/Entity Type

Plumber

Contact Information for Business Card

BRISCOMB PLUMBING
ABN 61 947 205 318 004

Harold Tenfield
Licensed Plumber 71635
Phone: 0477 261 408

27 Worrell Drive,
Penvarrow. 3847 Westhaven

Email: briscombplumbing@mailora.net

Logo Text

Briscomb Plumbing

Logo styles of interest
Character Logo
Wordmark Logo
Lettermark Logo

```html
<!DOCTYPE html>
<html lang="en">
<head>
<meta charset="utf-8">
<title>Briscomb Plumbing – Business Card</title>
<link rel="stylesheet" href="https://fonts.googleapis.com/css2?family=Source+Sans+3:wght@400;600;700&display=swap">
<style>
  :root {
    --lime: #b5d867;
    --lime-text: #a8d158;
    --paper: #ffffff;
    --card-edge: #bdbdbd;
  }
  * { margin: 0; padding: 0; box-sizing: border-box; }
  html, body {
    width: 1200px; height: 559px; overflow: hidden;
    background: var(--paper);
    font-family: "Source Sans 3", "Myriad Pro", Arial, sans-serif;
  }
  .canvas { position: relative; width: 1200px; height: 559px; }

  .card-front {
    position: absolute; left: 63px; top: 130px; width: 520px; height: 300px;
    background: var(--lime);
  }
  .front-brand {
    position: absolute; left: 114px; top: 108px;
    display: flex; align-items: flex-end; gap: 10px;
    color: var(--paper);
  }
  .front-brand .brand-square {
    width: 34px; height: 62px; background: var(--paper);
  }
  .front-brand .brand-name {
    font-weight: 600; font-size: 30px; line-height: 1; letter-spacing: -0.6px;
    margin-bottom: -3px;
  }

  .card-back {
    position: absolute; left: 615px; top: 130px; width: 521px; height: 300px;
    background: var(--paper); border: 1px solid var(--card-edge);
    color: var(--lime-text);
  }
  .back-brand { position: absolute; left: 33px; top: 33px; }
  .back-brand .brand-square {
    width: 24px; height: 44px; background: var(--lime-text); margin-bottom: 7px;
  }
  .back-brand .brand-name {
    font-weight: 700; font-size: 13px; line-height: 1; letter-spacing: -0.2px;
  }

  .contact {
    position: absolute; right: 30px; top: 97px; text-align: right;
  }
  .contact .person-name { font-weight: 700; font-size: 31px; line-height: 36px; }
  .contact .person-role { font-size: 15px; line-height: 20px; margin-bottom: 8px; }
  .contact .phone,
  .contact .email { font-weight: 600; font-size: 19px; line-height: 24px; }
  .contact .address { font-size: 15px; line-height: 18px; margin-top: 20px; }
</style>
</head>
<body>
<div class="canvas">
  <section class="card-front">
    <div class="front-brand">
      <span class="brand-square"></span>
      <span class="brand-name">BRISCOMB PLUMBING</span>
    </div>
  </section>

  <section class="card-back">
    <div class="back-brand">
      <div class="brand-square"></div>
      <div class="brand-name">BRISCOMB PLUMBING</div>
    </div>
    <div class="contact">
      <div class="person-name">Harold Tenfield</div>
      <div class="person-role">-&nbsp; Licensed Plumber</div>
      <div class="phone">0477 261 408 51 71635</div>
      <div class="email">briscombplumbing@mailora.net</div>
      <div class="address">Worrell Drive, Penvarrow. 3847 Westhaven<br>ABN 61 947 205 318 004</div>
    </div>
  </section>
</div>
</body>
</html>
```